Label Design VelmoRest Capsules

Hello dear designers!

We run a brand for dietary supplements and are looking for a talented designer to help take our brand to the next level. We are planning to launch new products with fresh packaging and redesigned labels. Additionally, we would like to refresh our company logo to make it fit better on the packaging.

Important Info:

Our brand: VelmoPure – specializing in products for detoxification, sleep, and eye protection.
Our shop: www.velmopure.at – currently offering two main products:
VelmoPure (Detox Tincture)
Velmo Optic Guard (Blue Light Filter Glasses)
Project Goal: Initially, we are looking for a label design for our new product VelmoRest (sleep capsules). If we like the design, we would like to revise the label for our first product, VelmoPure, and potentially rework our logo to make it more compact and visually appealing on our packaging.

Design Preferences: We are fans of the design style of Farv Nutra and would love a design in a similar style – modern, clean, and premium – but with a unique touch that fits our brand. You will find some inspirations and ideas that we particularly like in the attachment.

Important:

Our packaging for VelmoRest is an 8 OZ jar (similar to the smaller jars used by Farv Nutra).
The label should be clear, appealing, and give the product a high-quality look.
An example of a previous design draft (which hasn’t fully convinced us yet), along with inspirations for our upcoming bundle (including VelmoPure, VelmoRest, and VelmoOptic Guard), is also attached.
Special Opportunity: The designer with the best concept will have the chance to collaborate with us long-term! We have two more brands in the pipeline and are looking for a reliable and creative partner for future projects. Generous compensation and tips are guaranteed.

We look forward to seeing creative and professional designs that will take our brand to the next level!

Target Market(s)

Germany

Industry/Entity Type

Supplement

Font styles to use
Sans Serif

Colors

Designer to choose colors to be used in the design.

Requirements
Must have
• Es sollte Hochwertig und Modern aussehen. Matt schwarzer hintergrund. less is more
Nice to have
• Maybe The head should be visible in the background.
Should not have
• it should not be colorful, and not too playful, it should definitely not look cheap!

```html
<!DOCTYPE html>
<html lang="de">
<head>
<meta charset="UTF-8">
<title>VelmoRest Label</title>
<link rel="stylesheet" href="https://fonts.googleapis.com/css2?family=Montserrat:ital,wght@0,400;0,500;1,700;1,800&family=Oswald:wght@400;500;600&display=swap">
<style>
  :root {
    --bg: #efefef;
    --cyan: #4ec2e4;
    --cyan-light: #9fe2f4;
    --cyan-deep: #3fa9cb;
    --band-text: #c9f1fb;
    --ink: #0e0e0e;
    --ink-soft: #2b2b2b;
    --white: #f4f4f4;
  }
  * { margin: 0; padding: 0; box-sizing: border-box; }
  html, body {
    width: 1200px; height: 800px; overflow: hidden;
    background: var(--bg);
  }
  .canvas { position: relative; width: 1200px; height: 800px; }
  .label {
    position: absolute; left: 240px; top: 45px;
    width: 720px; height: 710px;
    border-radius: 6px; overflow: hidden;
    background: linear-gradient(90deg, var(--cyan-light) 0%, var(--cyan) 45%, var(--cyan-deep) 100%);
  }
  .label-shapes { position: absolute; inset: 0; }

  .supplement-row {
    position: absolute; left: 0; width: 720px;
    display: flex; justify-content: space-around;
    font-family: "Oswald", sans-serif; font-weight: 500;
    font-size: 11px; letter-spacing: 1.2px;
    color: var(--band-text);
  }
  .supplement-row.top { top: 19px; }
  .supplement-row.bottom { top: 684px; }

  .brand {
    position: absolute; left: 212px; top: 72px; width: 296px;
    display: flex; flex-direction: column; align-items: center; gap: 18px;
  }
  .brand-dot {
    width: 40px; height: 40px; border-radius: 50%;
    background: var(--white);
  }
  .brand-name {
    font-family: "Montserrat", sans-serif; font-weight: 400;
    font-size: 26px; letter-spacing: 5px; color: var(--white);
  }

  .product-title {
    position: absolute; left: 0; width: 720px; top: 255px;
    text-align: center;
    font-family: "Montserrat", sans-serif; font-style: italic; font-weight: 800;
    font-size: 62px; letter-spacing: 1px; color: var(--white);
  }
  .product-claim {
    position: absolute; left: 0; width: 720px; top: 332px;
    text-align: center;
    font-family: "Montserrat", sans-serif; font-style: italic; font-weight: 700;
    font-size: 21px; letter-spacing: 0.5px; color: var(--cyan);
  }

  .benefits {
    position: absolute; left: 178px; top: 390px; width: 364px;
    display: flex; justify-content: space-between;
  }
  .benefit {
    width: 112px; display: flex; flex-direction: column; align-items: center; gap: 14px;
  }
  .benefit-icon { width: 52px; height: 52px; }
  .benefit-text {
    font-family: "Oswald", sans-serif; font-weight: 500;
    font-size: 11px; line-height: 17px; text-align: center;
    color: var(--white);
  }

  .count {
    position: absolute; left: 0; width: 720px; top: 518px;
    text-align: center;
    font-family: "Oswald", sans-serif; font-weight: 600;
    font-size: 76px; line-height: 1; color: var(--cyan);
  }

  .bottom-band-text {
    position: absolute; top: 628px;
    font-family: "Oswald", sans-serif; font-weight: 500;
  }
  .servings { left: 70px; font-size: 27px; letter-spacing: 4px; color: var(--white); }
  .capsules { left: 279px; width: 163px; text-align: center; font-size: 34px; top: 622px; color: var(--white); }
  .night-supplement { left: 462px; font-size: 25px; color: var(--band-text); top: 630px; }
</style>
</head>
<body>
<div class="canvas">
  <div class="label">
    <svg class="label-shapes" width="720" height="710" viewBox="0 0 720 710" role="img" aria-label="Matte black panel with dark organic maze texture">
      <defs>
        <linearGradient id="panelGradient" x1="0" y1="0" x2="1" y2="0.3">
          <stop offset="0" stop-color="#3a3a3a"/>
          <stop offset="0.25" stop-color="#262626"/>
          <stop offset="0.6" stop-color="#121212"/>
          <stop offset="1" stop-color="#0b0b0b"/>
        </linearGradient>
      </defs>
      <path fill="url(#panelGradient)" d="M0,55 H150 C195,55 212,75 212,110 V150 C212,180 232,195 262,195 H458 C488,195 508,180 508,150 V110 C508,75 525,55 570,55 H720 V608 H480 C455,608 442,620 442,640 V650 C442,668 430,678 410,678 H310 C290,678 279,668 279,650 V640 C279,620 266,608 240,608 H0 Z"/>
    </svg>

    <div class="supplement-row top">
      <span>DIETARY SUPPLEMENT</span><span>DIETARY SUPPLEMENT</span><span>DIETARY SUPPLEMENT</span><span>DIETARY SUPPLEMENT</span><span>DIETARY SUPPLEMENT</span>
    </div>

    <div class="brand">
      <span class="brand-dot"></span>
      <span class="brand-name">VELMOPURE</span>
    </div>

    <h1 class="product-title">VELMO REST</h1>
    <p class="product-claim">FÖRDERT DIE TIEFSCHLAFPHASE</p>

    <div class="benefits">
      <div class="benefit">
        <svg class="benefit-icon" viewBox="0 0 52 52" aria-hidden="true">
          <g fill="var(--cyan)">
            <rect x="4" y="22" width="5" height="24" rx="1"/>
            <rect x="43" y="30" width="5" height="16" rx="1"/>
            <rect x="9" y="34" width="34" height="8" rx="1"/>
            <circle cx="16" cy="28" r="5"/>
            <rect x="22" y="24" width="20" height="9" rx="3"/>
            <circle cx="38" cy="11" r="6"/>
          </g>
          <path d="M38 7 V11 H41" stroke="#111" stroke-width="1.6" fill="none"/>
          <text x="18" y="12" font-family="Oswald, sans-serif" font-size="9" fill="var(--cyan)">z</text>
          <text x="24" y="8" font-family="Oswald, sans-serif" font-size="7" fill="var(--cyan)">z</text>
        </svg>
        <p class="benefit-text">ZWISCHENUBERSCHRIFT<br>HINZUFUGEN</p>
      </div>
      <div class="benefit">
        <svg class="benefit-icon" viewBox="0 0 52 52" aria-hidden="true">
          <g fill="var(--cyan)">
            <path d="M26 8 C33 16 33 30 26 38 C19 30 19 16 26 8 Z"/>
            <path d="M14 16 C22 20 25 30 24 38 C16 36 12 28 14 16 Z"/>
            <path d="M38 16 C30 20 27 30 28 38 C36 36 40 28 38 16 Z"/>
            <path d="M4 26 C12 26 20 32 22 40 C12 40 6 34 4 26 Z"/>
            <path d="M48 26 C40 26 32 32 30 40 C40 40 46 34 48 26 Z"/>
          </g>
        </svg>
        <p class="benefit-text">ZWISCHENUBERSCHRIFT<br>HINZUFUGEN</p>
      </div>
      <div class="benefit">
        <svg class="benefit-icon" viewBox="0 0 52 52" aria-hidden="true">
          <g fill="none" stroke="var(--cyan)" stroke-width="4" stroke-linecap="round">
            <path d="M9 30 A18 18 0 0 1 38 11"/>
            <path d="M43 22 A18 18 0 0 1 14 41"/>
          </g>
          <g fill="var(--cyan)">
            <path d="M34 5 L43 12 L33 16 Z"/>
            <path d="M18 47 L9 40 L19 36 Z"/>
            <path d="M28 13 L18 28 H25 L22 39 L33 23 H26 Z"/>
          </g>
        </svg>
        <p class="benefit-text">ZWISCHENUBERSCHRIFT<br>HINZUFUGEN</p>
      </div>
    </div>

    <div class="count">60</div>

    <span class="bottom-band-text servings">30 PORTIONEN</span>
    <span class="bottom-band-text capsules">KAPSELN</span>
    <span class="bottom-band-text night-supplement">NACHT-ERGÄNZUNG</span>

    <div class="supplement-row bottom">
      <span>DIETARY SUPPLEMENT</span><span>DIETARY SUPPLEMENT</span><span>DIETARY SUPPLEMENT</span><span>DIETARY SUPPLEMENT</span><span>DIETARY SUPPLEMENT</span>
    </div>
  </div>
</div>
</body>
</html>
```